Home Equity Lines of Credit
are BACK!!!

* Up to 97.5% on Owner Occupied Properties
* 700 Minimum Scores
* Fund in only 2-3 weeks

Can be used for...
* Education Expense
* Bill Consolidation
* Home Improvement
* Investments

Call today for more information!
(800) 647-2915

Bluecrest Lending Partners, Inc.
NMLS #318660
www.bluecrestlendhub.com

```html
<!DOCTYPE html>
<html lang="en">
<head>
<meta charset="UTF-8">
<title>Home Equity Lines of Credit are Back</title>
<link href="https://fonts.googleapis.com/css2?family=Jost:wght@400;500;600;700&family=Oswald:wght@700&display=swap" rel="stylesheet">
<style>
  :root {
    --navy: #135e86;
    --headline: #0f6391;
    --sky: #1a9be0;
    --ink: #2b2b2b;
    --white: #ffffff;
    --photo-warm: #d9cbb8;
    --photo-light: #efe8df;
  }
  * { margin: 0; padding: 0; box-sizing: border-box; }
  html, body { width: 1200px; height: 1200px; overflow: hidden; background: var(--white); }
  .flyer {
    position: relative; width: 1200px; height: 1200px;
    font-family: "Jost", sans-serif; color: var(--ink); background: var(--white);
  }
  .hero-photo {
    position: absolute; left: 0; top: 0; width: 640px; height: 586px;
    background: linear-gradient(90deg, var(--photo-warm) 0%, var(--photo-light) 70%, var(--white) 100%);
  }
  .headline { position: absolute; left: 608px; top: 78px; color: var(--headline); }
  .headline-lead { font-size: 45px; font-weight: 400; line-height: 62px; letter-spacing: 0.5px; }
  .headline-back {
    font-family: "Oswald", sans-serif; font-weight: 700; font-size: 158px;
    line-height: 1; margin-top: -6px; letter-spacing: 1px;
  }
  .benefits { position: absolute; left: 708px; top: 382px; list-style: none; font-size: 23px; line-height: 32px; }
  .benefits li { position: relative; padding-left: 42px; margin-bottom: 11px; }
  .benefits svg { position: absolute; left: 0; top: 9px; }
  .uses-band { position: absolute; left: 0; top: 586px; width: 1200px; height: 416px; background: var(--navy); }
  .uses-banner { position: absolute; left: 254px; top: 0; }
  .uses-title {
    position: absolute; left: 254px; top: 12px; width: 690px; text-align: center;
    color: var(--white); font-weight: 700; font-size: 36px; letter-spacing: 1px;
  }
  .use-item { position: absolute; top: 101px; width: 260px; text-align: center; }
  .use-photo {
    width: 196px; height: 196px; margin: 0 auto; border-radius: 50%;
    border: 5px solid var(--white);
  }
  .use-label {
    margin-top: 26px; height: 60px; display: flex; align-items: flex-end; justify-content: center;
    color: var(--white); font-weight: 700; font-size: 23px; line-height: 30px; letter-spacing: 0.3px;
  }
  .footer-strip { position: absolute; left: 0; top: 1177px; width: 1200px; height: 23px; background: var(--sky); }
  .call { position: absolute; left: 69px; top: 1038px; }
  .call-lead { color: var(--sky); font-size: 21px; line-height: 24px; }
  .call-phone { color: var(--navy); font-weight: 700; font-size: 41px; margin-top: 6px; letter-spacing: 0.5px; }
  .brand { position: absolute; left: 470px; top: 1072px; display: flex; align-items: center; gap: 10px; }
  .brand-dot { width: 26px; height: 26px; border-radius: 50%; background: var(--navy); }
  .brand-name { color: var(--navy); font-size: 20px; font-weight: 500; }
  .company { position: absolute; left: 792px; top: 1058px; font-size: 21px; line-height: 31px; }
  .company-web { color: var(--navy); }
</style>
</head>
<body>
<div class="flyer">
  <div class="hero-photo" role="img" aria-label="Smiling couple reviewing paperwork together at a laptop"></div>

  <div class="headline">
    <div class="headline-lead">Home Equity<br>Lines of Credit are</div>
    <div class="headline-back">BACK!!!</div>
  </div>

  <ul class="benefits">
    <li><svg width="18" height="16" viewBox="0 0 18 16"><path d="M2 8 L7 13 L16 2" fill="none" stroke="#2b2b2b" stroke-width="2"/></svg>Up to 97.5% on Owner<br>Occupied Properties</li>
    <li><svg width="18" height="16" viewBox="0 0 18 16"><path d="M2 8 L7 13 L16 2" fill="none" stroke="#2b2b2b" stroke-width="2"/></svg>700 Minimum Scores</li>
    <li><svg width="18" height="16" viewBox="0 0 18 16"><path d="M2 8 L7 13 L16 2" fill="none" stroke="#2b2b2b" stroke-width="2"/></svg>Fund in only 2-3 weeks</li>
  </ul>

  <section class="uses-band">
    <svg class="uses-banner" width="690" height="82" viewBox="0 0 690 82">
      <polygon points="0,0 690,0 655,80 35,80" fill="#0c3f5c" opacity="0.5" transform="translate(6,3)"/>
      <polygon points="0,0 690,0 655,78 35,78" fill="#1a9be0"/>
    </svg>
    <div class="uses-title">CAN BE USED FOR...</div>

    <div class="use-item" style="left:35px">
      <div class="use-photo" role="img" aria-label="Graduate in cap and gown holding a diploma" style="background:linear-gradient(160deg,#8a9a7c,#1f2a3c)"></div>
      <div class="use-label">EDUCATION<br>EXPENSE</div>
    </div>
    <div class="use-item" style="left:324px">
      <div class="use-photo" role="img" aria-label="Stressed couple on a sofa looking over bills" style="background:linear-gradient(160deg,#e4ddd6,#6b7a8c)"></div>
      <div class="use-label">BILL<br>CONSOLIDATION</div>
    </div>
    <div class="use-item" style="left:614px">
      <div class="use-photo" role="img" aria-label="Couple reviewing renovation plans in front of a brick wall" style="background:linear-gradient(160deg,#a86a52,#4a4c5c)"></div>
      <div class="use-label">HOME<br>IMPROVEMENT</div>
    </div>
    <div class="use-item" style="left:903px">
      <div class="use-photo" role="img" aria-label="Green seedling growing from a jar of coins" style="background:linear-gradient(180deg,#b8c4b6,#7d8a6c)"></div>
      <div class="use-label">INVESTMENTS</div>
    </div>
  </section>

  <div class="call">
    <div class="call-lead">Call today<br>for more information!</div>
    <div class="call-phone">(800) 647-2915</div>
  </div>

  <div class="brand">
    <span class="brand-dot"></span>
    <span class="brand-name">Bluecrest Lending Partners</span>
  </div>

  <div class="company">
    <div>Bluecrest Lending Partners, Inc.</div>
    <div>NMLS #318660</div>
    <div class="company-web">www.bluecrestlendhub.com</div>
  </div>

  <div class="footer-strip"></div>
</div>
</body>
</html>
```